Web Developer Needs a Business Card Design

I need a personal business card design that represents me as a web developer for potential employers. I would like the background to be a dark color on the front for contrast with my logo and name. The back will have all my information along with a smaller version of the logo. I want something with a modern look and feel, not too conservative. This will be used for potential employers and freelance work.

Industry/Entity Type

Business

Contact Information for Business Card

Front should have my logo and name. The back should have all my personal information which would include: name: Tom Brevardi, phone: 570-614-9083, email: tombrevardi@mailwisp.com, website url: www.tombrevardi.com, logo, web developer.

Font styles to use
Sans Serif

Requirements
Must have
• Must include my logo. The color palette base color will be the logo color.

```html
<!DOCTYPE html>
<html lang="en">
<head>
<meta charset="utf-8">
<title>Tom Brevardi – Business Card</title>
<link rel="stylesheet" href="https://fonts.googleapis.com/css2?family=Mulish:wght@400;500&display=swap">
<style>
  :root {
    --page: #ffffff;
    --frame-dark: #231f20;
    --frame-light: #cbcccd;
    --card-dark: #130720;
    --card-dark-sheen: #2d2540;
    --card-light: #f3f3f5;
    --teal: #86d9cb;
    --divider: #a7a6ad;
    --ink-grey: #77767a;
  }
  html, body {
    margin: 0;
    padding: 0;
    width: 1008px;
    height: 1200px;
    overflow: hidden;
    background: var(--page);
    font-family: "Mulish", "Helvetica Neue", Arial, sans-serif;
  }
  .canvas { position: relative; width: 1008px; height: 1200px; }

  .card-frame { position: absolute; left: 176px; width: 656px; height: 364px; border-radius: 14px; }
  .card-frame--front { top: 216px; background: var(--frame-dark); }
  .card-frame--back { top: 627px; background: var(--frame-light); }

  .card { position: absolute; left: 27px; top: 28px; width: 601px; height: 309px; overflow: hidden; }
  .card--front {
    background: linear-gradient(135deg, var(--card-dark) 0%, var(--card-dark) 52%, var(--card-dark-sheen) 62%, var(--card-dark-sheen) 100%);
  }
  .card--back { background: var(--card-light); }

  .brand-mark { position: absolute; left: 164px; top: 113px; width: 82px; height: 82px; }
  .brand-divider { position: absolute; left: 287px; top: 128px; width: 2px; height: 56px; background: var(--divider); }
  .front-name {
    position: absolute; left: 319px; top: 143px; margin: 0;
    font-size: 22px; font-weight: 400; letter-spacing: 0.5px;
    color: var(--teal); text-transform: uppercase; line-height: 22px;
  }

  .brand-mark--large { position: absolute; left: -3px; top: -3px; width: 340px; height: 320px; }

  .contact { position: absolute; left: 383px; top: 168px; color: var(--ink-grey); white-space: nowrap; }
  .contact__name { font-size: 20px; font-weight: 400; text-transform: uppercase; line-height: 1; margin: 0; }
  .contact__role { font-size: 12px; text-transform: uppercase; letter-spacing: 0.3px; margin: 4px 0 0; line-height: 1; }
  .contact__list { list-style: none; margin: 22px 0 0; padding: 0; font-size: 15px; line-height: 20px; }
</style>
</head>
<body>
<main class="canvas">
  <section class="card-frame card-frame--front" aria-label="Card front">
    <div class="card card--front">
      <svg class="brand-mark" viewBox="0 0 82 82" aria-label="Tom Brevardi monogram">
        <circle cx="41" cy="41" r="37" fill="none" stroke="var(--teal)" stroke-width="5"/>
        <text x="41" y="49" text-anchor="middle" font-family="Mulish, sans-serif" font-size="24" font-weight="500" fill="var(--teal)">TB</text>
      </svg>
      <span class="brand-divider"></span>
      <h1 class="front-name">Tom Brevardi</h1>
    </div>
  </section>

  <section class="card-frame card-frame--back" aria-label="Card back">
    <div class="card card--back">
      <svg class="brand-mark--large" viewBox="0 0 340 320" aria-label="Tom Brevardi monogram">
        <circle cx="164" cy="159" r="157" fill="none" stroke="var(--teal)" stroke-width="14"/>
        <text x="164" y="196" text-anchor="middle" font-family="Mulish, sans-serif" font-size="110" font-weight="500" fill="var(--teal)">TB</text>
      </svg>
      <div class="contact">
        <h2 class="contact__name">Tom Brevardi</h2>
        <p class="contact__role">Web Developer</p>
        <ul class="contact__list">
          <li>570-614-9083</li>
          <li>tombrevardi@mailwisp.com</li>
          <li>www.tombrevardi.com</li>
        </ul>
      </div>
    </div>
  </section>
</main>
</body>
</html>
```